Norvale Works - pioneers of next generation consulting!

We are a next generation management consulting firm with two focus areas and USPs (unique selling points):>Technology driven business developmentWe are not developers, we are experts in HOW to apply and incorporate technology in your business dna to drive business growth and value-added change.>Creating high performing teams levering our philosophy of collective intelligence. We truly understand the need of human engagement and we know that the only way of getting there is by building strong relationships among people, a warm and open culture is a stepping stone towards effective collaboration within/among teams. - We don't want a ”corporate feel” to our templates. The organic feeling we have with our blue-on-blue blobs has the idea of ever changing movement and shape changing. Please see our website, www.norvaleworks.se. - In our context we sit among classic business mgmt. consultants and classic IT mgmt. consultants. We cater to business, tech and humans as the ultimate vehicle of change and business value. -To have a clean template one suggestion is to only use blue, white and black and keeping other colors separate, as an alternative but we are truly open allow your creativity add value to this. We are looking to find a slide deck which we can pick slides from, depending on what/whom/why we interact with customer we want to create different outcomes and our presentations should support this.

Industry/Entity Type

Management Consulting

Requirements
Must have
• next generation powerpoint and how to package storytelling. please keep to our look and feel, we just arrived at our logo, colours and shapes. Help us to carry it into our ppt's as well.
Should not have
• Hi all, please have a look at our website. It is still very new and more will be done, but our goal is to make powerpoint to come alive again and mirror our pioneering hearts and brains.

```html
<!DOCTYPE html>
<html lang="en">
<head>
<meta charset="utf-8">
<title>Norvale Works – Presentation Template</title>
<link href="https://fonts.googleapis.com/css2?family=Open+Sans:wght@400;600;700;800&family=Permanent+Marker&family=Space+Mono&display=swap" rel="stylesheet">
<style>
:root{
  --page:#e8e8e9;
  --navy:#163f86;
  --blue:#1f5bb5;
  --mid:#3b78cf;
  --light:#8db3e6;
  --pale:#dde8f6;
  --green:#3aa85a;
  --ink:#222;
  --grey:#6a6a6a;
  --white:#fff;
}
*{margin:0;padding:0;box-sizing:border-box}
html,body{width:1200px;height:2769px;overflow:hidden;background:var(--page)}
.canvas{position:relative;width:1200px;height:2769px}
.slide{position:absolute;width:351px;height:197px;background:var(--white);box-shadow:0 2px 5px rgba(0,0,0,.18);display:block}
.hero{width:525px;height:295px}
.hero-left{left:79px;top:157px}
.hero-right{left:620px;top:157px}
.c0{left:37px}.c1{left:425px}.c2{left:812px}
.r0{top:701px}.r1{top:930px}.r2{top:1159px}.r3{top:1388px}.r4{top:1617px}
.r5{top:1846px}.r6{top:2075px}.r7{top:2304px}.r8{top:2533px}
.mk{font-family:'Permanent Marker',cursive;fill:var(--blue)}
.mono{font-family:'Space Mono',monospace}
.sans{font-family:'Open Sans',sans-serif}
.brand{font-family:'Open Sans',sans-serif;font-weight:800;letter-spacing:.5px}
.tiny{font-family:'Open Sans',sans-serif;font-size:4px;fill:var(--grey)}
.bold{font-weight:700}
.w{fill:var(--white)}
.blue{fill:var(--blue)}
.green{fill:var(--green)}
.navy{fill:var(--navy)}
.mid{fill:var(--mid)}
.light{fill:var(--light)}
.pale{fill:var(--pale)}
.ink{fill:var(--ink)}
.mid-center{text-anchor:middle}
.defs{position:absolute;width:0;height:0}
</style>
</head>
<body>
<svg class="defs" aria-hidden="true">
  <defs>
    <linearGradient id="photo" x1="0" y1="0" x2="1" y2="1">
      <stop offset="0" stop-color="#5a6478"/>
      <stop offset=".5" stop-color="#a39488"/>
      <stop offset="1" stop-color="#3b4558"/>
    </linearGradient>
    <linearGradient id="photoBlue" x1="0" y1="0" x2="1" y2="1">
      <stop offset="0" stop-color="#3a5f9e"/>
      <stop offset="1" stop-color="#1b3f7c"/>
    </linearGradient>
    <symbol id="footer" viewBox="0 0 351 22">
      <path d="M0 9 C80 0 170 16 351 4 V22 H0Z" fill="#8db3e6"/>
      <path d="M0 13 C100 6 210 18 351 10 V22 H0Z" fill="#1f5bb5"/>
      <text x="8" y="19" class="brand w" font-size="5.5">NORVALE WORKS</text>
      <text x="335" y="19" class="sans w" font-size="3.5">Page 1</text>
    </symbol>
  </defs>
</svg>

<main class="canvas">

<!-- hero: title slide -->
<svg class="slide hero hero-left" viewBox="0 0 351 197">
  <g role="img" aria-label="Workshop photo, hands at a table, tinted blue"><rect width="351" height="135" fill="url(#photoBlue)"/></g>
  <rect width="351" height="135" fill="#1f5bb5" opacity=".55"/>
  <path d="M0 112 C100 88 210 132 351 100 V197 H0Z" fill="#8db3e6"/>
  <path d="M0 122 C90 100 190 142 351 112 V197 H0Z" fill="#fff"/>
  <text x="175" y="46" class="mk w mid-center" font-size="13">PRESENTATION TITLE</text>
  <rect x="140" y="50" width="70" height="1" fill="#fff"/>
  <text x="175" y="62" class="mono light mid-center" font-size="8">Sub Presentation Title</text>
  <text x="175" y="80" class="mono w mid-center" font-size="6">April, 2019</text>
  <text x="175" y="168" class="brand blue mid-center" font-size="12">NORVALE WORKS</text>
</svg>

<!-- hero: circle title slide -->
<svg class="slide hero hero-right" viewBox="0 0 351 197">
  <g role="img" aria-label="Workshop photo, person working with electronics"><rect width="351" height="197" fill="url(#photo)"/></g>
  <rect width="351" height="197" fill="#1b3f7c" opacity=".35"/>
  <circle cx="175" cy="98" r="74" fill="#3b78cf" opacity=".75"/>
  <text x="175" y="62" class="brand w mid-center" font-size="7">NORVALE WORKS</text>
  <rect x="160" y="67" width="30" height=".8" fill="#fff"/>
  <text x="175" y="84" class="mk w mid-center" font-size="9">PRESENTATION</text>
  <text x="175" y="95" class="mk w mid-center" font-size="9">TITLE</text>
  <text x="175" y="107" class="mono w mid-center" font-size="5.5">Sub Presentation Title</text>
  <text x="175" y="128" class="mono w mid-center" font-size="5">April, 2019</text>
</svg>

<!-- row 0 -->
<svg class="slide c0 r0" viewBox="0 0 351 197">
  <g role="img" aria-label="Workshop photo, hands working with electronics"><rect width="351" height="197" fill="url(#photo)"/></g>
  <rect width="351" height="197" fill="#1b3f7c" opacity=".35"/>
  <circle cx="110" cy="95" r="72" fill="#3b78cf" opacity=".75"/>
  <text x="110" y="60" class="brand w mid-center" font-size="7">NORVALE WORKS</text>
  <rect x="95" y="65" width="30" height=".8" fill="#fff"/>
  <text x="110" y="83" class="mk w mid-center" font-size="9">PRESENTATION</text>
  <text x="110" y="94" class="mk w mid-center" font-size="9">TITLE</text>
  <text x="110" y="106" class="mono w mid-center" font-size="5.5">Sub Presentation Title</text>
  <text x="110" y="126" class="mono w mid-center" font-size="5">April, 2019</text>
</svg>

<svg class="slide c1 r0" viewBox="0 0 351 197">
  <g role="img" aria-label="Workshop photo tinted blue"><rect width="351" height="135" fill="url(#photoBlue)"/></g>
  <rect width="351" height="135" fill="#1f5bb5" opacity=".55"/>
  <path d="M0 112 C100 88 210 132 351 100 V197 H0Z" fill="#8db3e6"/>
  <path d="M0 122 C90 100 190 142 351 112 V197 H0Z" fill="#fff"/>
  <text x="175" y="46" class="mk w mid-center" font-size="13">PRESENTATION TITLE</text>
  <rect x="140" y="50" width="70" height="1" fill="#fff"/>
  <text x="175" y="62" class="mono light mid-center" font-size="8">Sub Presentation Title</text>
  <text x="175" y="80" class="mono w mid-center" font-size="6">April, 2019</text>
  <text x="175" y="168" class="brand blue mid-center" font-size="12">NORVALE WORKS</text>
</svg>

<svg class="slide c2 r0" viewBox="0 0 351 197">
  <g role="img" aria-label="Workshop photo tinted blue"><rect width="351" height="135" fill="url(#photoBlue)"/></g>
  <rect width="351" height="135" fill="#1f5bb5" opacity=".55"/>
  <path d="M0 112 C100 88 210 132 351 100 V197 H0Z" fill="#8db3e6"/>
  <path d="M0 122 C90 100 190 142 351 112 V197 H0Z" fill="#fff"/>
  <text x="175" y="46" class="mk w mid-center" font-size="13">PRESENTATION TITLE</text>
  <rect x="140" y="50" width="70" height="1" fill="#fff"/>
  <text x="175" y="62" class="mono light mid-center" font-size="8">Sub Presentation Title</text>
  <text x="175" y="80" class="mono w mid-center" font-size="6">April, 2019</text>
  <text x="175" y="168" class="brand blue mid-center" font-size="12">NORVALE WORKS</text>
</svg>

<!-- row 1 -->
<svg class="slide c0 r1" viewBox="0 0 351 197">
  <g role="img" aria-label="Photo of people talking in a workshop"><rect width="351" height="197" fill="url(#photo)"/></g>
  <path d="M230 0 H351 V197 H160 C120 150 150 100 190 70 C210 50 200 20 230 0Z" fill="#1f5bb5"/>
  <text x="215" y="88" class="mk w" font-size="9">SECTION SLIDE</text>
  <text x="215" y="100" class="mono light" font-size="5">Sub Divider</text>
  <text x="215" y="108" class="mono light" font-size="5">Presentation</text>
</svg>

<svg class="slide c1 r1" viewBox="0 0 351 197">
  <path d="M0 0 H165 C200 60 145 125 190 197 H0Z" fill="#1f5bb5"/>
  <text x="20" y="48" class="mk w" font-size="10">TABLE OF</text>
  <text x="20" y="61" class="mk w" font-size="10">CONTENT</text>
  <g class="sans">
    <text x="200" y="33" class="bold blue" font-size="11">01</text><text x="220" y="28" class="mk" font-size="5.5">ABOUT US</text><text x="220" y="34" class="tiny">Lorem ipsum dolor sit amet.</text>
    <text x="200" y="57" class="bold blue" font-size="11">02</text><text x="220" y="52" class="mk" font-size="5.5">HOW WE DO</text><text x="220" y="58" class="tiny">Lorem ipsum dolor sit amet.</text>
    <text x="200" y="81" class="bold blue" font-size="11">03</text><text x="220" y="76" class="mk" font-size="5.5">BUSINESS PROCESS</text><text x="220" y="82" class="tiny">Lorem ipsum dolor sit amet.</text>
    <text x="200" y="105" class="bold blue" font-size="11">04</text><text x="220" y="100" class="mk" font-size="5.5">OUR TEAM</text><text x="220" y="106" class="tiny">Lorem ipsum dolor sit amet.</text>
    <text x="200" y="129" class="bold blue" font-size="11">05</text><text x="220" y="124" class="mk" font-size="5.5">OUR ACTIVITY</text><text x="220" y="130" class="tiny">Lorem ipsum dolor sit amet.</text>
    <text x="200" y="153" class="bold blue" font-size="11">06</text><text x="220" y="148" class="mk" font-size="5.5">CONTACT US</text><text x="220" y="154" class="tiny">Lorem ipsum dolor sit amet.</text>
  </g>
</svg>

<svg class="slide c2 r1" viewBox="0 0 351 197">
  <text x="10" y="18" class="mk" font-size="8">ONE COLUMN</text>
  <text x="10" y="32" class="sans bold ink" font-size="5">Lorem Ipsum</text>
  <g class="tiny">
    <text x="12" y="44">• Lorem ipsum dolor sit amet, te ullum corpora delicata duo. Rebum insolens per.</text>
    <text x="18" y="51">• Sint brute et usu, duo nusquam apeirian.</text>
    <text x="12" y="62">• Lorem ipsum dolor sit amet, te ullum corpora delicata duo. Rebum insolens per.</text>
    <text x="18" y="69">• Sint brute et usu, duo nusquam apeirian.</text>
    <text x="12" y="80">• Lorem ipsum dolor sit amet, te ullum corpora delicata duo. Rebum insolens per.</text>
    <text x="18" y="87">• Sint brute et usu, duo nusquam apeirian.</text>
    <text x="12" y="98">• Lorem ipsum dolor sit amet, te ullum corpora delicata duo. Rebum insolens per.</text>
    <text x="18" y="105">• Sint brute et usu, duo nusquam apeirian.</text>
  </g>
  <use href="#footer" x="0" y="175" width="351" height="22"/>
</svg>

<!-- row 2 -->
<svg class="slide c0 r2" viewBox="0 0 351 197">
  <rect width="351" height="197" fill="#1f5bb5"/>
  <text x="10" y="18" class="mk w" font-size="8">ONE COLUMN</text>
  <text x="10" y="32" class="sans bold w" font-size="5">Lorem Ipsum</text>
  <g class="sans w" font-size="4">
    <text x="12" y="44">• Lorem ipsum dolor sit amet, te ullum corpora delicata duo. Rebum insolens per.</text>
    <text x="18" y="51">• Sint brute et usu, duo nusquam apeirian.</text>
    <text x="12" y="62">• Lorem ipsum dolor sit amet, te ullum corpora delicata duo. Rebum insolens per.</text>
    <text x="18" y="69">• Sint brute et usu, duo nusquam apeirian.</text>
    <text x="12" y="80">• Lorem ipsum dolor sit amet, te ullum corpora delicata duo. Rebum insolens per.</text>
    <text x="18" y="87">• Sint brute et usu, duo nusquam apeirian.</text>
  </g>
  <use href="#footer" x="0" y="175" width="351" height="22"/>
</svg>

<svg class="slide c1 r2" viewBox="0 0 351 197">
  <text x="10" y="18" class="mk" font-size="8">LEFT COLUMN</text>
  <text x="10" y="40" class="sans bold ink" font-size="5">Lorem Ipsum</text>
  <rect x="10" y="48" width="140" height="13" fill="#1f5bb5"/><text x="16" y="56" class="sans w" font-size="4">Lorem ipsum dolor sit amet, te ullum corpora.</text>
  <rect x="10" y="66" width="140" height="13" fill="#163f86"/><text x="16" y="74" class="sans w" font-size="4">Lorem ipsum dolor sit amet, te ullum corpora.</text>
  <rect x="10" y="84" width="140" height="13" fill="#1f5bb5"/><text x="16" y="92" class="sans w" font-size="4">Lorem ipsum dolor sit amet, te ullum corpora.</text>
  <rect x="10" y="102" width="140" height="13" fill="#3b78cf"/><text x="16" y="110" class="sans w" font-size="4">Lorem ipsum dolor sit amet, te ullum corpora.</text>
  <path d="M180 40 C230 15 330 25 335 70 C345 120 320 160 260 165 C200 170 170 120 180 40Z" fill="#dde8f6"/>
  <text x="260" y="40" class="sans ink mid-center" font-size="5">Bar Chart Sample</text>
  <line x1="205" y1="150" x2="320" y2="150" stroke="#999" stroke-width=".5"/>
  <g>
    <rect x="212" y="110" width="7" height="40" fill="#163f86"/><rect x="220" y="120" width="7" height="30" fill="#3aa85a"/><rect x="228" y="100" width="7" height="50" fill="#8db3e6"/>
    <rect x="248" y="95" width="7" height="55" fill="#163f86"/><rect x="256" y="112" width="7" height="38" fill="#3aa85a"/><rect x="264" y="70" width="7" height="80" fill="#8db3e6"/>
    <rect x="284" y="80" width="7" height="70" fill="#163f86"/><rect x="292" y="104" width="7" height="46" fill="#3aa85a"/><rect x="300" y="90" width="7" height="60" fill="#8db3e6"/>
  </g>
  <text x="225" y="156" class="tiny">Category 1</text><text x="255" y="156" class="tiny">Category 2</text><text x="288" y="156" class="tiny">Category 3</text>
  <use href="#footer" x="0" y="175" width="351" height="22"/>
</svg>

<svg class="slide c2 r2" viewBox="0 0 351 197">
  <rect width="175" height="197" fill="#1f5bb5"/>
  <text x="180" y="18" class="mk" font-size="8">RIGHT COLUMN</text>
  <g role="img" aria-label="Photo of a small humanoid robot"><path d="M12 20 H150 C162 70 150 130 160 160 H12Z" fill="url(#photo)"/></g>
  <text x="20" y="155" class="mono w" font-size="4">LOREM IPSUM DOLOR SIT AMET</text>
  <text x="185" y="36" class="mk" font-size="6">LOREM IPSUM</text>
  <g class="tiny">
    <text x="185" y="48">• Lorem ipsum dolor sit amet, te ullum corpora delicata.</text>
    <text x="191" y="55">• Sint brute et usu, duo nusquam apeirian.</text>
    <text x="185" y="66">• Lorem ipsum dolor sit amet, te ullum corpora delicata.</text>
    <text x="191" y="73">• Sint brute et usu, duo nusquam apeirian.</text>
    <text x="185" y="84">• Lorem ipsum dolor sit amet, te ullum corpora delicata.</text>
    <text x="191" y="91">• Sint brute et usu, duo nusquam apeirian.</text>
    <text x="185" y="102">• Lorem ipsum dolor sit amet, te ullum corpora delicata.</text>
    <text x="191" y="109">• Sint brute et usu, duo nusquam apeirian.</text>
  </g>
  <use href="#footer" x="0" y="175" width="351" height="22"/>
</svg>

<!-- row 3 -->
<svg class="slide c0 r3" viewBox="0 0 351 197">
  <g role="img" aria-label="Photo of a group of smiling people taking a selfie"><rect width="351" height="197" fill="url(#photo)"/></g>
  <use href="#footer" x="0" y="175" width="351" height="22"/>
</svg>

<svg class="slide c1 r3" viewBox="0 0 351 197">
  <path d="M0 0 H351 V60 C250 80 100 45 0 70Z" fill="#163f86"/>
  <text x="175" y="30" class="sans bold w mid-center" font-size="9">RIGHT COLUMN</text>
  <g>
    <rect x="35" y="55" width="80" height="100" fill="#fff" stroke="#d5dcea" stroke-width=".6"/>
    <rect x="67" y="62" width="16" height="14" fill="#dde8f6"/><rect x="71" y="66" width="8" height="6" fill="none" stroke="#1f5bb5" stroke-width="1"/>
    <text x="75" y="90" class="mk mid-center" font-size="6">TEXT HERE</text>
    <text x="75" y="100" class="tiny mid-center">Lorem ipsum dolor sit amet,</text>
    <text x="75" y="106" class="tiny mid-center">te ullum corpora delicata.</text>
    <text x="75" y="112" class="tiny mid-center">No alia tota modus qui.</text>
    <rect x="35" y="153" width="80" height="2" fill="#1f5bb5"/>
  </g>
  <g>
    <rect x="135" y="55" width="80" height="100" fill="#fff" stroke="#d5dcea" stroke-width=".6"/>
    <rect x="167" y="62" width="16" height="14" fill="#dde8f6"/><circle cx="175" cy="69" r="4" fill="none" stroke="#1f5bb5" stroke-width="1"/>
    <text x="175" y="90" class="mk mid-center" font-size="6">TEXT HERE</text>
    <text x="175" y="100" class="tiny mid-center">Lorem ipsum dolor sit amet,</text>
    <text x="175" y="106" class="tiny mid-center">te ullum corpora delicata.</text>
    <text x="175" y="112" class="tiny mid-center">No alia tota modus qui.</text>
    <rect x="135" y="153" width="80" height="2" fill="#1f5bb5"/>
  </g>
  <g>
    <rect x="235" y="55" width="80" height="100" fill="#fff" stroke="#d5dcea" stroke-width=".6"/>
    <rect x="267" y="62" width="16" height="14" fill="#e2f3e7"/><path d="M270 69 L274 73 L281 65" fill="none" stroke="#3aa85a" stroke-width="1.2"/>
    <text x="275" y="90" class="mk green mid-center" font-size="6">TEXT HERE</text>
    <text x="275" y="100" class="tiny mid-center">Lorem ipsum dolor sit amet,</text>
    <text x="275" y="106" class="tiny mid-center">te ullum corpora delicata.</text>
    <text x="275" y="112" class="tiny mid-center">No alia tota modus qui.</text>
    <rect x="235" y="153" width="80" height="2" fill="#3aa85a"/>
  </g>
  <use href="#footer" x="0" y="175" width="351" height="22"/>
</svg>

<svg class="slide c2 r3" viewBox="0 0 351 197">
  <g role="img" aria-label="Photo of a consultant presenting to a colleague"><rect width="351" height="197" fill="url(#photo)"/></g>
  <path d="M0 105 C40 95 95 92 125 130 C145 160 135 185 115 197 H0Z" fill="#1f5bb5"/>
  <text x="12" y="148" class="mk w" font-size="9">SECTION SLIDE</text>
  <text x="12" y="160" class="mono light" font-size="5">Sub Divider</text>
  <text x="12" y="168" class="mono light" font-size="5">Presentation</text>
</svg>

<!-- row 4 -->
<svg class="slide c0 r4" viewBox="0 0 351 197">
  <text x="10" y="18" class="mk" font-size="8">COLLABORATION PICS</text>
  <g role="img" aria-label="Small round photos of team collaboration">
    <circle cx="32" cy="58" r="17" fill="url(#photo)"/><circle cx="147" cy="58" r="17" fill="url(#photo)"/><circle cx="318" cy="58" r="17" fill="url(#photo)"/>
    <circle cx="32" cy="125" r="17" fill="url(#photo)"/><circle cx="147" cy="125" r="17" fill="url(#photo)"/><circle cx="318" cy="125" r="17" fill="url(#photo)"/>
  </g>
  <g>
    <text x="55" y="52" class="mk" font-size="4.5">1. HEADING SAMPLE</text><text x="55" y="59" class="tiny">Lorem ipsum dolor sit amet,</text><text x="55" y="65" class="tiny">te ullum corpora delicata.</text>
    <text x="170" y="52" class="mk" font-size="4.5">2. HEADING SAMPLE</text><text x="170" y="59" class="tiny">Lorem ipsum dolor sit amet,</text><text x="170" y="65" class="tiny">te ullum corpora delicata.</text>
    <text x="240" y="52" class="mk" font-size="4.5">3. HEADING SAMPLE</text><text x="240" y="59" class="tiny">Lorem ipsum dolor sit,</text><text x="240" y="65" class="tiny">te ullum corpora.</text>
    <text x="55" y="119" class="mk" font-size="4.5">4. HEADING SAMPLE</text><text x="55" y="126" class="tiny">Lorem ipsum dolor sit amet,</text><text x="55" y="132" class="tiny">te ullum corpora delicata.</text>
    <text x="170" y="119" class="mk" font-size="4.5">5. HEADING SAMPLE</text><text x="170" y="126" class="tiny">Lorem ipsum dolor sit amet,</text><text x="170" y="132" class="tiny">te ullum corpora delicata.</text>
    <text x="240" y="119" class="mk" font-size="4.5">6. HEADING SAMPLE</text><text x="240" y="126" class="tiny">Lorem ipsum dolor sit,</text><text x="240" y="132" class="tiny">te ullum corpora.</text>
  </g>
  <use href="#footer" x="0" y="175" width="351" height="22"/>
</svg>

<svg class="slide c1 r4" viewBox="0 0 351 197">
  <rect width="351" height="197" fill="#1f5bb5"/>
  <path d="M215 0 H351 V197 H235 C195 150 255 120 225 65 C208 35 218 12 215 0Z" fill="#fff"/>
  <g role="img" aria-label="Portrait photo of a consultant in a suit"><ellipse cx="290" cy="100" rx="45" ry="62" fill="url(#photo)"/></g>
  <text x="18" y="30" class="sans bold w" font-size="9">JOHN DOE</text>
  <text x="18" y="38" class="sans light" font-size="4">Lorem ipsum dolor sit amet,</text>
  <text x="14" y="62" class="sans bold light" font-size="18">“</text>
  <g class="sans w" font-size="4.2">
    <text x="26" y="56">Lorem Ipsum is simply dummy text of the</text>
    <text x="26" y="63">printing and industry. Lorem Ipsum has been</text>
    <text x="26" y="70">the industry's standard dummy text ever since</text>
    <text x="26" y="77">the 1500s, when an unknown printer took a</text>
    <text x="26" y="84">galley of type and scrambled it to make a type</text>
    <text x="26" y="91">specimen book.</text>
  </g>
  <text x="140" y="102" class="sans bold light" font-size="18">”</text>
  <text x="26" y="104" class="sans light" font-size="4">– John Doe</text>
  <use href="#footer" x="0" y="175" width="351" height="22"/>
</svg>

<svg class="slide c2 r4" viewBox="0 0 351 197">
  <rect width="351" height="197" fill="#1f5bb5"/>
  <path d="M20 10 C60 60 40 120 90 160" fill="none" stroke="#3b78cf" stroke-width="6" opacity=".6"/>
  <path d="M300 20 C280 70 320 110 290 160" fill="none" stroke="#3b78cf" stroke-width="6" opacity=".6"/>
  <circle cx="175" cy="72" r="7" fill="#fff"/>
  <text x="175" y="77" class="sans bold blue mid-center" font-size="9">“</text>
  <text x="175" y="95" class="sans w mid-center" font-size="5.5">Lorem ipsum dolor sit amet, te ullum corpora delicata duo. Rebum</text>
  <text x="175" y="103" class="sans w mid-center" font-size="5.5">insolens pri eu. No alia tota modus qui.</text>
  <text x="175" y="118" class="sans light mid-center" font-size="4.5">– John Doe</text>
  <use href="#footer" x="0" y="175" width="351" height="22"/>
</svg>

<!-- row 5 -->
<svg class="slide c0 r5" viewBox="0 0 351 197">
  <text x="10" y="18" class="mk" font-size="8">CONTENT WITH ICONS</text>
  <g>
    <rect x="20" y="30" width="95" height="22" fill="#fff" stroke="#dbe2ee" stroke-width=".6"/><rect x="117" y="31" width="16" height="16" rx="3" fill="#1f5bb5"/>
    <text x="85" y="38" class="mk" font-size="4.5">HEADING 1</text><text x="50" y="46" class="tiny">Lorem ipsum dolor sit amet, consectetur.</text>
    <rect x="20" y="58" width="95" height="22" fill="#fff" stroke="#dbe2ee" stroke-width=".6"/><rect x="117" y="59" width="16" height="16" rx="3" fill="#1f5bb5"/>
    <text x="85" y="66" class="mk" font-size="4.5">HEADING 2</text><text x="50" y="74" class="tiny">Lorem ipsum dolor sit amet, consectetur.</text>
    <rect x="20" y="86" width="95" height="22" fill="#fff" stroke="#dbe2ee" stroke-width=".6"/><rect x="117" y="87" width="16" height="16" rx="3" fill="#3aa85a"/>
    <text x="85" y="94" class="mk green" font-size="4.5">HEADING 3</text><text x="50" y="102" class="tiny">Lorem ipsum dolor sit amet, consectetur.</text>
    <rect x="143" y="31" width="16" height="16" rx="3" fill="#1f5bb5"/><rect x="161" y="30" width="95" height="22" fill="#fff" stroke="#dbe2ee" stroke-width=".6"/>
    <text x="168" y="38" class="mk" font-size="4.5">HEADING 4</text><text x="168" y="46" class="tiny">Lorem ipsum dolor sit amet, consectetur.</text>
    <rect x="143" y="59" width="16" height="16" rx="3" fill="#1f5bb5"/><rect x="161" y="58" width="95" height="22" fill="#fff" stroke="#dbe2ee" stroke-width=".6"/>
    <text x="168" y="66" class="mk" font-size="4.5">HEADING 5</text><text x="168" y="74" class="tiny">Lorem ipsum dolor sit amet, consectetur.</text>
    <rect x="143" y="87" width="16" height="16" rx="3" fill="#3aa85a"/><rect x="161" y="86" width="95" height="22" fill="#fff" stroke="#dbe2ee" stroke-width=".6"/>
    <text x="168" y="94" class="mk green" font-size="4.5">HEADING 6</text><text x="168" y="102" class="tiny">Lorem ipsum dolor sit amet, consectetur.</text>
  </g>
  <use href="#footer" x="0" y="175" width="351" height="22"/>
</svg>

<svg class="slide c1 r5" viewBox="0 0 351 197">
  <text x="10" y="18" class="mk" font-size="8">THE "3 CIRCLES" SLIDE</text>
  <circle cx="110" cy="85" r="38" fill="#2a4272"/>
  <circle cx="240" cy="85" r="38" fill="#2a4272"/>
  <circle cx="175" cy="85" r="38" fill="#5b8fd6" opacity=".9"/>
  <text x="110" y="100" class="sans bold w mid-center" font-size="5">CULTURE</text>
  <text x="175" y="98" class="sans bold w mid-center" font-size="5">BUSINESS</text>
  <text x="175" y="104" class="sans bold w mid-center" font-size="5">INTENT</text>
  <text x="240" y="100" class="sans bold w mid-center" font-size="5">TECHNOLOGY</text>
  <path d="M145 80 l4 4 l-4 4 M205 80 l-4 4 l4 4" fill="none" stroke="#fff" stroke-width="1"/>
  <g class="tiny">
    <text x="110" y="140" class="mid-center">Lorem ipsum dolor sit amet, te ullum</text><text x="110" y="146" class="mid-center">corpora delicata duo. Rebum insolens.</text>
    <text x="175" y="140" class="mid-center">Lorem ipsum dolor sit amet, te ullum</text><text x="175" y="146" class="mid-center">corpora delicata duo. Rebum insolens.</text>
    <text x="240" y="140" class="mid-center">Lorem ipsum dolor sit amet, te ullum</text><text x="240" y="146" class="mid-center">corpora delicata duo. Rebum insolens.</text>
  </g>
  <use href="#footer" x="0" y="175" width="351" height="22"/>
</svg>

<svg class="slide c2 r5" viewBox="0 0 351 197">
  <text x="10" y="18" class="mk" font-size="8">OUR CONSULTANTS</text>
  <path d="M22 60 C30 35 70 40 72 70 C74 100 40 110 25 95Z" fill="#1f5bb5"/>
  <path d="M102 55 C120 35 150 50 148 80 C146 105 110 105 105 90Z" fill="#1f5bb5"/>
  <path d="M185 60 C195 40 230 45 228 75 C226 102 190 106 184 88Z" fill="#1f5bb5"/>
  <path d="M262 58 C280 38 312 52 308 82 C305 104 270 104 265 88Z" fill="#1f5bb5"/>
  <g role="img" aria-label="Portrait photos of four consultants">
    <rect x="35" y="45" width="30" height="60" rx="12" fill="url(#photo)"/>
    <rect x="112" y="45" width="30" height="60" rx="12" fill="url(#photo)"/>
    <rect x="195" y="45" width="30" height="60" rx="12" fill="url(#photo)"/>
    <rect x="272" y="45" width="30" height="60" rx="12" fill="url(#photo)"/>
  </g>
  <g class="sans bold ink" font-size="4.5">
    <text x="50" y="118" class="mid-center">Miles Haverty</text>
    <text x="127" y="118" class="mid-center">Ada Lindqvist</text>
    <text x="210" y="118" class="mid-center">Karl Ostrow</text>
    <text x="287" y="118" class="mid-center">Tessa Varnholm</text>
  </g>
  <g class="tiny">
    <text x="50" y="126" class="mid-center">Lorem ipsum dolor sit</text><text x="50" y="132" class="mid-center">amet, consectetur.</text>
    <text x="127" y="126" class="mid-center">Lorem ipsum dolor sit</text><text x="127" y="132" class="mid-center">amet, consectetur.</text>
    <text x="210" y="126" class="mid-center">Lorem ipsum dolor sit</text><text x="210" y="132" class="mid-center">amet, consectetur.</text>
    <text x="287" y="126" class="mid-center">Lorem ipsum dolor sit</text><text x="287" y="132" class="mid-center">amet, consectetur.</text>
  </g>
  <use href="#footer" x="0" y="175" width="351" height="22"/>
</svg>

<!-- row 6 -->
<svg class="slide c0 r6" viewBox="0 0 351 197">
  <text x="10" y="18" class="mk" font-size="8">GRAPH SLIDES SAMPLE</text>
  <circle cx="175" cy="92" r="32" fill="none" stroke="#3b78cf" stroke-width="20" stroke-dasharray="23.1 2"/>
  <circle cx="175" cy="92" r="32" fill="none" stroke="#163f86" stroke-width="20" stroke-dasharray="23.1 27.1"/>
  <circle cx="175" cy="92" r="19" fill="#163f86"/>
  <text x="175" y="91" class="brand w mid-center" font-size="4.5">NORVALE</text>
  <text x="175" y="97" class="brand w mid-center" font-size="4.5">WORKS</text>
  <g class="tiny">
    <text x="15" y="50">Lorem ipsum dolor sit amet,</text><text x="15" y="56">consectetur adipiscing elit.</text>
    <text x="15" y="90">Lorem ipsum dolor sit amet,</text><text x="15" y="96">consectetur adipiscing elit.</text>
    <text x="15" y="130">Lorem ipsum dolor sit amet,</text><text x="15" y="136">consectetur adipiscing elit.</text>
    <text x="250" y="50">Lorem ipsum dolor sit amet,</text><text x="250" y="56">consectetur adipiscing elit.</text>
    <text x="250" y="90">Lorem ipsum dolor sit amet,</text><text x="250" y="96">consectetur adipiscing elit.</text>
    <text x="250" y="130">Lorem ipsum dolor sit amet,</text><text x="250" y="136">consectetur adipiscing elit.</text>
  </g>
  <use href="#footer" x="0" y="175" width="351" height="22"/>
</svg>

<svg class="slide c1 r6" viewBox="0 0 351 197">
  <text x="10" y="18" class="mk" font-size="8">DATA SAMPLE</text>
  <g fill="none" stroke-width="6">
    <circle cx="60" cy="68" r="18" stroke="#e3e8f0"/>
    <circle cx="60" cy="68" r="18" stroke="#1f5bb5" stroke-dasharray="28.3 113.1" transform="rotate(-90 60 68)"/>
    <circle cx="175" cy="68" r="18" stroke="#e3e8f0"/>
    <circle cx="175" cy="68" r="18" stroke="#1f5bb5" stroke-dasharray="55.4 113.1" transform="rotate(-90 175 68)"/>
    <circle cx="290" cy="68" r="18" stroke="#e3e8f0"/>
    <circle cx="290" cy="68" r="18" stroke="#1f5bb5" stroke-dasharray="79.2 113.1" transform="rotate(-90 290 68)"/>
  </g>
  <text x="60" y="71" class="mk ink mid-center" font-size="8">25%</text>
  <text x="175" y="71" class="mk ink mid-center" font-size="8">49%</text>
  <text x="290" y="71" class="mk ink mid-center" font-size="8">70%</text>
  <g>
    <text x="60" y="106" class="mk mid-center" font-size="5.5">LOREM IPSUM</text><text x="60" y="114" class="tiny mid-center">Lorem ipsum dolor sit amet,</text><text x="60" y="120" class="tiny mid-center">te ullum corpora. No alia</text><text x="60" y="126" class="tiny mid-center">tota modus qui.</text>
    <text x="175" y="106" class="mk mid-center" font-size="5.5">LOREM IPSUM</text><text x="175" y="114" class="tiny mid-center">Lorem ipsum dolor sit amet,</text><text x="175" y="120" class="tiny mid-center">te ullum corpora. No alia</text><text x="175" y="126" class="tiny mid-center">tota modus qui.</text>
    <text x="290" y="106" class="mk mid-center" font-size="5.5">LOREM IPSUM</text><text x="290" y="114" class="tiny mid-center">Lorem ipsum dolor sit amet,</text><text x="290" y="120" class="tiny mid-center">te ullum corpora. No alia</text><text x="290" y="126" class="tiny mid-center">tota modus qui.</text>
  </g>
  <use href="#footer" x="0" y="175" width="351" height="22"/>
</svg>

<svg class="slide c2 r6" viewBox="0 0 351 197">
  <text x="10" y="18" class="mk" font-size="8">TIMELINE SAMPLE</text>
  <g>
    <rect x="30" y="94" width="48" height="12" fill="#163f86"/><rect x="78" y="94" width="48" height="12" fill="#3b78cf"/>
    <rect x="126" y="94" width="48" height="12" fill="#163f86"/><rect x="174" y="94" width="48" height="12" fill="#3b78cf"/>
    <rect x="222" y="94" width="48" height="12" fill="#163f86"/><rect x="270" y="94" width="40" height="12" fill="#3b78cf"/>
    <path d="M310 90 L324 100 L310 110Z" fill="#3b78cf"/>
  </g>
  <g class="sans bold w" font-size="5">
    <text x="54" y="102" class="mid-center">2010</text><text x="102" y="102" class="mid-center">2011</text><text x="150" y="102" class="mid-center">2012</text>
    <text x="198" y="102" class="mid-center">2013</text><text x="246" y="102" class="mid-center">2014</text><text x="292" y="102" class="mid-center">2015</text>
  </g>
  <g fill="#163f86">
    <rect x="49" y="78" width="10" height="10" rx="2"/><rect x="145" y="78" width="10" height="10" rx="2"/><rect x="241" y="78" width="10" height="10" rx="2"/>
    <rect x="97" y="112" width="10" height="10" rx="2"/><rect x="193" y="112" width="10" height="10" rx="2"/><rect x="287" y="112" width="10" height="10" rx="2"/>
  </g>
  <g class="tiny">
    <text x="54" y="62" class="mid-center">Lorem ipsum dolor sit</text><text x="54" y="68" class="mid-center">amet, consectetur.</text>
    <text x="150" y="62" class="mid-center">Lorem ipsum dolor sit</text><text x="150" y="68" class="mid-center">amet, consectetur.</text>
    <text x="246" y="62" class="mid-center">Lorem ipsum dolor sit</text><text x="246" y="68" class="mid-center">amet, consectetur.</text>
    <text x="102" y="132" class="mid-center">Lorem ipsum dolor sit</text><text x="102" y="138" class="mid-center">amet, consectetur.</text>
    <text x="198" y="132" class="mid-center">Lorem ipsum dolor sit</text><text x="198" y="138" class="mid-center">amet, consectetur.</text>
    <text x="292" y="132" class="mid-center">Lorem ipsum dolor sit</text><text x="292" y="138" class="mid-center">amet, consectetur.</text>
  </g>
  <use href="#footer" x="0" y="175" width="351" height="22"/>
</svg>

<!-- row 7 -->
<svg class="slide c0 r7" viewBox="0 0 351 197">
  <path d="M0 0 H351 V72 C260 105 130 62 0 100Z" fill="#163f86"/>
  <text x="175" y="20" class="mk w mid-center" font-size="8">CONTENT WITH ICONS</text>
  <text x="175" y="34" class="sans w mid-center" font-size="4.5">Lorem ipsum dolor sit amet, te ullum corpora delicata duo.</text>
  <text x="175" y="41" class="sans w mid-center" font-size="4.5">Rebum insolens pri eu. No alia tota modus qui.</text>
  <circle cx="62" cy="96" r="9" fill="#1f5bb5" stroke="#fff" stroke-width="1.5"/>
  <circle cx="175" cy="100" r="9" fill="#3b78cf" stroke="#fff" stroke-width="1.5"/>
  <circle cx="290" cy="80" r="9" fill="#3aa85a" stroke="#fff" stroke-width="1.5"/>
  <path d="M58 96 L61 99 L66 93 M171 100 L174 103 L179 97 M286 80 L289 83 L294 77" fill="none" stroke="#fff" stroke-width="1"/>
  <g>
    <text x="62" y="118" class="mk mid-center" font-size="5.5">HEADING 1</text><text x="62" y="126" class="tiny mid-center">Lorem ipsum dolor sit amet,</text><text x="62" y="132" class="tiny mid-center">consectetur adipiscing elit.</text>
    <text x="175" y="122" class="mk mid-center" font-size="5.5">HEADING 2</text><text x="175" y="130" class="tiny mid-center">Lorem ipsum dolor sit amet,</text><text x="175" y="136" class="tiny mid-center">consectetur adipiscing elit.</text>
    <text x="290" y="102" class="mk green mid-center" font-size="5.5">HEADING 3</text><text x="290" y="110" class="tiny mid-center">Lorem ipsum dolor sit amet,</text><text x="290" y="116" class="tiny mid-center">consectetur adipiscing elit.</text>
  </g>
  <use href="#footer" x="0" y="175" width="351" height="22"/>
</svg>

<svg class="slide c1 r7" viewBox="0 0 351 197">
  <text x="10" y="18" class="mk" font-size="8">CHART SAMPLE</text>
  <text x="175" y="34" class="sans ink mid-center" font-size="5">LOREM IPSUM DOLOR SIT AMET</text>
  <line x1="40" y1="42" x2="40" y2="150" stroke="#ccc" stroke-width=".5"/>
  <line x1="40" y1="150" x2="320" y2="150" stroke="#ccc" stroke-width=".5"/>
  <g>
    <rect x="50" y="95" width="9" height="55" fill="#163f86"/>
    <rect x="72" y="110" width="9" height="40" fill="#1f5bb5"/>
    <rect x="94" y="100" width="9" height="50" fill="#3aa85a"/>
    <rect x="116" y="85" width="9" height="65" fill="#163f86"/>
    <rect x="138" y="105" width="9" height="45" fill="#1f5bb5"/>
    <rect x="160" y="122" width="9" height="28" fill="#3b78cf"/>
    <rect x="182" y="115" width="9" height="35" fill="#3aa85a"/>
    <rect x="204" y="60" width="9" height="90" fill="#163f86"/>
    <rect x="226" y="108" width="9" height="42" fill="#1f5bb5"/>
    <rect x="248" y="122" width="9" height="28" fill="#3aa85a"/>
    <rect x="270" y="95" width="9" height="55" fill="#163f86"/>
    <rect x="292" y="110" width="9" height="40" fill="#1f5bb5"/>
  </g>
  <use href="#footer" x="0" y="175" width="351" height="22"/>
</svg>

<svg class="slide c2 r7" viewBox="0 0 351 197">
  <text x="10" y="18" class="mk" font-size="8">CONTENT WITH IMAGE</text>
  <g role="img" aria-label="Grid of workshop and team photos">
    <rect x="0" y="28" width="88" height="70" fill="url(#photo)"/>
    <rect x="88" y="28" width="88" height="70" fill="url(#photo)"/>
    <rect x="176" y="28" width="88" height="70" fill="url(#photo)"/>
    <rect x="88" y="98" width="88" height="72" fill="url(#photo)"/>
    <rect x="264" y="98" width="87" height="72" fill="url(#photo)"/>
  </g>
  <rect x="264" y="28" width="87" height="70" fill="#1f5bb5"/>
  <rect x="0" y="98" width="88" height="72" fill="#163f86"/>
  <rect x="176" y="98" width="88" height="72" fill="#1f5bb5"/>
  <text x="272" y="45" class="mk w" font-size="5">HEADING 1</text><text x="272" y="53" class="sans w" font-size="3.8">Lorem ipsum dolor sit</text><text x="272" y="59" class="sans w" font-size="3.8">amet, consectetur.</text>
  <text x="8" y="115" class="mk w" font-size="5">HEADING 2</text><text x="8" y="123" class="sans w" font-size="3.8">Lorem ipsum dolor sit</text><text x="8" y="129" class="sans w" font-size="3.8">amet, consectetur.</text>
  <text x="184" y="115" class="mk w" font-size="5">HEADING 3</text><text x="184" y="123" class="sans w" font-size="3.8">Lorem ipsum dolor sit</text><text x="184" y="129" class="sans w" font-size="3.8">amet, consectetur.</text>
  <use href="#footer" x="0" y="175" width="351" height="22"/>
</svg>

<!-- row 8 -->
<svg class="slide c0 r8" viewBox="0 0 351 197">
  <path d="M40 20 C100 0 160 30 150 90 C145 150 90 175 40 160 C0 150 -10 60 40 20Z" fill="#8db3e6"/>
  <g role="img" aria-label="Photo of a consultant working at a laptop"><path d="M30 30 C90 10 145 40 140 95 C135 150 85 168 35 152 C0 140 -5 60 30 30Z" fill="url(#photo)"/></g>
  <text x="175" y="48" class="mk" font-size="8">PRESENTATION TITLE</text>
  <g class="tiny">
    <text x="175" y="60">Lorem ipsum dolor sit amet, te ullum corpora</text>
    <text x="175" y="66">delicata duo. Rebum insolens pri eu.</text>
    <text x="175" y="72">No alia tota modus qui.</text>
    <text x="175" y="84">Sint brute et usu. Duo nusquam apeirian</text>
    <text x="175" y="90">adversarium et.</text>
  </g>
  <use href="#footer" x="0" y="175" width="351" height="22"/>
</svg>

<svg class="slide c1 r8" viewBox="0 0 351 197">
  <text x="15" y="40" class="mk" font-size="8">PRESENTATION TITLE</text>
  <g class="tiny">
    <text x="15" y="52">Lorem ipsum dolor sit amet, te ullum corpora</text>
    <text x="15" y="58">delicata duo. Rebum insolens pri eu.</text>
    <text x="15" y="64">No alia tota modus qui.</text>
    <text x="15" y="76">Sint brute et usu. Duo nusquam apeirian</text>
    <text x="15" y="82">adversarium et.</text>
  </g>
  <path d="M210 25 C270 0 340 30 335 90 C330 150 270 175 215 158 C170 140 165 50 210 25Z" fill="#8db3e6"/>
  <g role="img" aria-label="Photo of smiling colleagues at an event"><path d="M200 30 C260 8 330 38 325 92 C320 148 265 168 210 152 C170 138 162 55 200 30Z" fill="url(#photo)"/></g>
  <use href="#footer" x="0" y="175" width="351" height="22"/>
</svg>

<svg class="slide c2 r8" viewBox="0 0 351 197">
  <g role="img" aria-label="Close-up photo with soft blurred background"><rect width="351" height="197" fill="url(#photo)"/></g>
  <rect width="351" height="197" fill="#1b3f7c" opacity=".25"/>
  <path d="M175 25 C225 25 245 60 240 100 C235 145 200 160 165 158 C125 156 105 125 110 90 C115 50 135 25 175 25Z" fill="#1f5bb5" opacity=".88"/>
  <text x="175" y="70" class="brand w mid-center" font-size="7">NORVALE WORKS</text>
  <rect x="160" y="76" width="30" height=".8" fill="#fff"/>
  <text x="175" y="94" class="mk w mid-center" font-size="9">THANK YOU</text>
  <text x="175" y="122" class="sans w mid-center" font-size="4.5">www.norvaleworks.se</text>
</svg>

</main>
</body>
</html>
```